K & D A/C Compressors' Business Card

Hello,

I need someone to create a new business card for my business. The name of my Business is: K & D A/C Compressors. I sell automotive air conditioning parts (a/c parts). I would like the business card to incorporate my logo, and to have an automotive feel to it. It is important that the business card feel like it is coming from an automotive parts business.

I already have a logo, which I will provide.

Thanks.
Updates

Project Deadline Extended Reason: I feel like extending the deadline until October 9, 2017, will allow for more time to design the business card. Thank you for your understanding. Added Monday, October 2, 2017

Target Market(s)

Consumers who need automotive a/c parts, and auto mechanics.

Industry/Entity Type

Automotive

Contact Information for Business Card

Business name: K & D A/C Compressors
Business Address: 48207 Southwest 36th Street, North Miami Beach, Florida 33162
Telephone: 305-472-1390
Fax: To be provided once I choose your design.
Website: www.kdcoolunits.example
Email: support@kdcoolunits.example
Names: To be provided once I choose your design.

Font styles to use
Sans Serif

Colors

Designer to choose colors to be used in the design.

Requirements
Must have
• The business card must include all of the "Business Card Details" and the logo I have uploaded.

```html
<!DOCTYPE html>
<html lang="en">
<head>
<meta charset="utf-8">
<title>K &amp; D A/C Compressors – Business Card</title>
<link rel="stylesheet" href="https://fonts.googleapis.com/css2?family=Roboto:wght@300;400;500;700&family=Roboto+Condensed:wght@500;700&display=swap">
<style>
  :root {
    --stage: #2b2b2b;
    --brand-blue: #0aaeea;
    --paper: #f4f4f4;
    --ink: #444444;
    --ink-soft: #9a9a9a;
    --logo-grey: #8f8f8f;
    --rule: #555555;
    --white: #ffffff;
  }
  * { margin: 0; padding: 0; box-sizing: border-box; }
  html, body {
    width: 1200px; height: 960px; overflow: hidden;
    background: var(--stage);
    font-family: "Roboto", Arial, sans-serif;
  }
  .canvas { position: relative; width: 1200px; height: 960px; }

  .card {
    position: absolute; left: 320px; width: 600px;
    border-radius: 18px; overflow: hidden;
  }

  /* Front */
  .card--front {
    top: 105px; height: 345px;
    background: var(--brand-blue);
    color: var(--white);
  }
  .card--front .brand-name {
    position: absolute; left: 0; right: 0; top: 120px;
    text-align: center;
    font-size: 44px; font-weight: 500; line-height: 1.1;
    color: var(--white);
  }
  .card--front .website {
    position: absolute; left: 0; right: 0; top: 284px;
    text-align: center;
    font-size: 14px; font-weight: 400; letter-spacing: 4px;
  }

  /* Back */
  .card--back {
    top: 493px; height: 342px;
    background: var(--paper);
    color: var(--ink);
    border-bottom: 6px solid var(--brand-blue);
  }
  .card--back .brand-name {
    position: absolute; right: 40px; top: 48px;
    text-align: right;
    font-size: 34px; font-weight: 500; line-height: 1.15;
    color: var(--logo-grey);
  }
  .person { position: absolute; left: 30px; top: 186px; }
  .person__name {
    font-family: "Roboto Condensed", Arial, sans-serif;
    font-weight: 700; font-size: 22px; color: var(--brand-blue);
    letter-spacing: 0.3px;
  }
  .person__title {
    font-size: 14px; font-weight: 500; color: var(--ink-soft);
    margin-top: 2px;
  }
  .divider {
    position: absolute; left: 30px; right: 38px; top: 236px;
    height: 1px; background: var(--rule);
  }
  .contact-list {
    position: absolute; left: 30px; top: 248px;
    list-style: none; font-size: 14px; line-height: 19.5px;
  }
  .contact-list li { display: flex; align-items: center; gap: 8px; }
  .contact-list svg { width: 14px; height: 14px; fill: var(--brand-blue); flex: none; }
  .address {
    position: absolute; right: 37px; top: 250px;
    text-align: right; font-size: 14px; line-height: 18.5px;
    font-style: normal;
  }
  .address .website { letter-spacing: 1.2px; }
</style>
</head>
<body>
<main class="canvas">

  <section class="card card--front" aria-label="Business card front">
    <div class="brand-name">K &amp; D<br>A/C Compressors</div>
    <div class="website">www.kdcoolunits.example</div>
  </section>

  <section class="card card--back" aria-label="Business card back">
    <div class="brand-name">K &amp; D<br>A/C Compressors</div>

    <div class="person">
      <div class="person__name">DANIEL REYES</div>
      <div class="person__title">CEO/FOUNDER</div>
    </div>

    <div class="divider"></div>

    <ul class="contact-list">
      <li>
        <svg viewBox="0 0 24 24" aria-hidden="true"><path d="M6.6 10.8a15.2 15.2 0 0 0 6.6 6.6l2.2-2.2c.3-.3.7-.4 1-.2 1.1.4 2.3.6 3.6.6.6 0 1 .4 1 1V20c0 .6-.4 1-1 1A17 17 0 0 1 3 4c0-.6.4-1 1-1h3.5c.6 0 1 .4 1 1 0 1.3.2 2.5.6 3.6.1.3 0 .7-.2 1z"/></svg>
        <span>305-472-1390</span>
      </li>
      <li>
        <svg viewBox="0 0 24 24" aria-hidden="true"><path d="M6 2h12v5H6z"/><path d="M3 8h18a1 1 0 0 1 1 1v8h-4v5H6v-5H2V9a1 1 0 0 1 1-1zm5 7v5h8v-5z"/></svg>
        <span>305-472-1391</span>
      </li>
      <li>
        <svg viewBox="0 0 24 24" aria-hidden="true"><path d="M2 5h20v2l-10 6L2 7z"/><path d="M2 9l10 6 10-6v10H2z"/></svg>
        <span>support@kdcoolunits.example</span>
      </li>
    </ul>

    <address class="address">
      48207 Southwest 36th Street<br>
      North Miami Beach, Florida 33162<br>
      <span class="website">www.kdcoolunits.example</span>
    </address>
  </section>

</main>
</body>
</html>
```